Brivora Collective Business Card Design

We need a business card design for Brivora Collective. We are a healthcare recruiting, wellness and education company. We partner with medical facilities to find quality candidates. We also offer free wellness courses.
The final design should communicate an emphasis on recruiting and wellness
The main purpose of the business card is to utilized it for networking events, give to hospitals, executives, VCs surgery centers and clinics. I want it to be sleek, clean, use of our brand colors and professional.

```html
<!DOCTYPE html>
<html lang="en">
<head>
<meta charset="UTF-8">
<title>Brivora Collective – Business Card</title>
<link href="https://fonts.googleapis.com/css2?family=Arimo:wght@400;700&display=swap" rel="stylesheet">
<style>
  :root {
    --brand-green: #04594f;
    --card-white: #ffffff;
    --ink: #2b2b2b;
    --backdrop: #e9ebea;
    --card-shadow: rgba(0, 0, 0, 0.12);
  }
  * { margin: 0; padding: 0; box-sizing: border-box; }
  html, body {
    width: 1200px;
    height: 900px;
    overflow: hidden;
    background: var(--backdrop);
    font-family: "Arimo", Arial, sans-serif;
  }
  .canvas {
    position: relative;
    width: 1200px;
    height: 900px;
  }
  .card {
    position: absolute;
    left: 280px;
    width: 640px;
    height: 366px;
    box-shadow: 0 6px 18px var(--card-shadow);
  }
  .card--front {
    top: 44px;
    background: var(--card-white);
  }
  .card--back {
    top: 470px;
    background: var(--brand-green);
  }

  /* Front */
  .holder {
    position: absolute;
    left: 41px;
    top: 40px;
  }
  .holder__name {
    font-weight: 700;
    font-size: 23px;
    letter-spacing: 0.2px;
    color: var(--brand-green);
    line-height: 1.05;
  }
  .holder__role {
    font-size: 16px;
    color: var(--ink);
    margin-top: 2px;
  }
  .contact {
    position: absolute;
    left: 41px;
    top: 218px;
    font-size: 16px;
    color: var(--ink);
    line-height: 20px;
  }
  .contact__address { margin-bottom: 14px; }
  .contact__list { list-style: none; }
  .contact__item {
    display: flex;
    align-items: center;
    gap: 6px;
  }
  .contact__icon {
    width: 12px;
    height: 12px;
    flex: none;
  }
  .wordmark {
    position: absolute;
    right: 42px;
    top: 120px;
    display: flex;
    flex-direction: column;
    align-items: center;
    gap: 12px;
  }
  .wordmark__square {
    width: 34px;
    height: 34px;
    border-radius: 4px;
    background: var(--brand-green);
  }
  .wordmark__name {
    font-weight: 400;
    font-size: 30px;
    line-height: 1.05;
    text-align: center;
    color: var(--brand-green);
  }

  /* Back */
  .back-wordmark {
    position: absolute;
    right: 58px;
    top: 146px;
    display: flex;
    align-items: center;
    gap: 22px;
  }
  .back-wordmark__square {
    width: 60px;
    height: 60px;
    border-radius: 6px;
    background: var(--card-white);
  }
  .back-wordmark__name {
    font-weight: 400;
    font-size: 40px;
    line-height: 1.05;
    color: var(--card-white);
  }
</style>
</head>
<body>
<main class="canvas">

  <section class="card card--front" aria-label="Business card front">
    <div class="holder">
      <h1 class="holder__name">DANIEL MERCER</h1>
      <p class="holder__role">Director</p>
    </div>

    <div class="contact">
      <p class="contact__address">2170 Linden Park Rd Maple<br>Hollow, GA 30418</p>
      <ul class="contact__list">
        <li class="contact__item">
          <svg class="contact__icon" viewBox="0 0 12 12" aria-hidden="true">
            <path d="M3 1.2 L4.6 3.4 L3.8 4.6 C4.4 6 5.6 7.4 7.2 8.2 L8.4 7.4 L10.6 9 L9.6 10.8 C5.6 10.4 1.8 6.6 1.2 2.4 Z" fill="var(--brand-green)"/>
          </svg>
          <span>470-555-0182</span>
        </li>
        <li class="contact__item">
          <svg class="contact__icon" viewBox="0 0 12 12" aria-hidden="true">
            <rect x="1" y="2.5" width="10" height="7" fill="none" stroke="var(--brand-green)" stroke-width="1.3"/>
            <path d="M1 2.8 L6 6.6 L11 2.8" fill="none" stroke="var(--brand-green)" stroke-width="1.3"/>
          </svg>
          <span>info@brivoracollective.com</span>
        </li>
        <li class="contact__item">
          <svg class="contact__icon" viewBox="0 0 12 12" aria-hidden="true">
            <circle cx="6" cy="6" r="5" fill="none" stroke="var(--brand-green)" stroke-width="1.1"/>
            <ellipse cx="6" cy="6" rx="2.2" ry="5" fill="none" stroke="var(--brand-green)" stroke-width="1"/>
            <path d="M1 6 H11 M1.8 3.5 H10.2 M1.8 8.5 H10.2" stroke="var(--brand-green)" stroke-width="0.9"/>
          </svg>
          <span>www.brivoracollective.com</span>
        </li>
      </ul>
    </div>

    <div class="wordmark">
      <span class="wordmark__square" aria-hidden="true"></span>
      <p class="wordmark__name">Brivora<br>Collective</p>
    </div>
  </section>

  <section class="card card--back" aria-label="Business card back">
    <div class="back-wordmark">
      <span class="back-wordmark__square" aria-hidden="true"></span>
      <p class="back-wordmark__name">Brivora<br>Collective</p>
    </div>
  </section>

</main>
</body>
</html>
```